Business Card Design Project

I have attached the logo and the colour pallete for the branding for the company.

Creative designs for business cards are needed.

The Company is modern corporate.

Industry/Entity Type

Business

```html
<!DOCTYPE html>
<html lang="en">
<head>
<meta charset="utf-8">
<title>Wayforth Business Card</title>
<link rel="stylesheet" href="https://fonts.googleapis.com/css2?family=Source+Sans+3:wght@400;600;700&display=swap">
<style>
  :root {
    --backdrop: #ece9e4;
    --paper: #ffffff;
    --plum: #6a2a69;
    --plum-deep: #3e1540;
    --plum-mid: #6b2b6b;
    --ink: #444444;
    --ink-soft: #555555;
    --rule-red: #d9324a;
    --rule-orange: #f08a24;
    --card-edge: #2b2b2b;
  }
  * { box-sizing: border-box; margin: 0; padding: 0; }
  html, body {
    width: 1200px; height: 1006px; overflow: hidden;
    background: var(--backdrop);
    font-family: "Source Sans 3", "Myriad Pro", sans-serif;
  }
  .canvas { position: relative; width: 1200px; height: 1006px; }
  .card {
    position: absolute; top: 36px;
    width: 529px; height: 926px;
  }
  .card--front { left: 43px; background: var(--paper); border: 1px solid var(--card-edge); }
  .card--back {
    left: 615px;
    background: linear-gradient(90deg, var(--plum-deep) 0%, var(--plum-mid) 50%, var(--plum-deep) 100%);
  }
  .wordmark {
    position: absolute; left: 0; right: 0;
    text-align: center; font-weight: 700;
    font-size: 100px; line-height: 1; letter-spacing: -1px;
  }
  .card--front .wordmark { top: 105px; color: var(--plum); }
  .card--back .wordmark { top: 392px; color: var(--paper); }
  .rule {
    position: absolute; left: 0; right: 0; height: 3px;
    background: linear-gradient(90deg, var(--rule-red), var(--rule-orange));
  }
  .rule--top { top: 372px; }
  .rule--bottom { top: 492px; }
  .name-band {
    position: absolute; left: 0; right: 0; top: 380px; height: 109px;
    background: var(--plum); color: var(--paper); text-align: center;
  }
  .name-band__name { font-weight: 600; font-size: 40px; line-height: 1; margin-top: 16px; }
  .name-band__title { font-weight: 400; font-size: 29px; line-height: 1; margin-top: 9px; }
  .contact-list { position: absolute; left: 0; right: 0; top: 546px; list-style: none; }
  .contact-list li {
    display: flex; justify-content: center; align-items: center; gap: 10px;
    height: 50px; font-size: 30px; color: var(--ink);
  }
  .contact-list svg { width: 24px; height: 24px; fill: none; stroke: var(--plum); stroke-width: 1.6; }
  .address {
    position: absolute; left: 0; right: 0; top: 804px;
    text-align: center; font-size: 29px; line-height: 40px; color: var(--ink-soft);
  }
  .back-url {
    position: absolute; left: 0; right: 0; top: 815px;
    text-align: center; color: var(--paper); font-size: 30px; letter-spacing: 0.32em;
  }
</style>
</head>
<body>
<main class="canvas">
  <section class="card card--front">
    <div class="wordmark">wayforth</div>
    <div class="rule rule--top"></div>
    <div class="name-band">
      <p class="name-band__name">Your Name</p>
      <p class="name-band__title">Title</p>
    </div>
    <div class="rule rule--bottom"></div>
    <ul class="contact-list">
      <li>
        <svg viewBox="0 0 24 24" aria-hidden="true"><circle cx="12" cy="12" r="10.5"/><path d="M9 6.5l2 3-1.3 1.2c.8 1.6 1.9 2.8 3.5 3.6L14.5 13l3 2-1.5 2.2C11.5 16.5 8 13 7 8z" fill="var(--plum)" stroke="none"/></svg>
        <span>123-456-0789</span>
      </li>
      <li>
        <svg viewBox="0 0 24 24" aria-hidden="true"><rect x="7" y="5" width="10" height="17" rx="1.5" fill="var(--plum)" stroke="none"/><line x1="15" y1="5" x2="15" y2="1"/><rect x="8.8" y="7" width="6.4" height="5" fill="#fff" stroke="none"/><g fill="#fff" stroke="none"><rect x="9" y="14" width="1.6" height="1.4"/><rect x="11.2" y="14" width="1.6" height="1.4"/><rect x="13.4" y="14" width="1.6" height="1.4"/><rect x="9" y="16.6" width="1.6" height="1.4"/><rect x="11.2" y="16.6" width="1.6" height="1.4"/><rect x="13.4" y="16.6" width="1.6" height="1.4"/></g></svg>
        <span>123-456-0789</span>
      </li>
      <li>
        <svg viewBox="0 0 24 24" aria-hidden="true"><path d="M2 10l10-6 10 6v11H2z" fill="var(--plum)" stroke="none"/><rect x="6" y="7" width="12" height="7" fill="#fff" stroke="none"/><path d="M8 9h8M8 11h8" stroke-width="1"/><path d="M2 21l8-7h4l8 7" stroke="#fff" stroke-width="1.2"/></svg>
        <span>info@wayforth.com</span>
      </li>
      <li>
        <svg viewBox="0 0 24 24" aria-hidden="true"><circle cx="12" cy="12" r="10"/><ellipse cx="12" cy="12" rx="4.5" ry="10"/><path d="M2 12h20M4 7h16M4 17h16M12 2v20"/></svg>
        <span>www.wayforth.com</span>
      </li>
    </ul>
    <p class="address">Street Name, City Name<br>State Zip Code</p>
  </section>
  <section class="card card--back">
    <div class="wordmark">wayforth</div>
    <p class="back-url">www.wayforth.com</p>
  </section>
</main>
</body>
</html>
```